Site for company producing and selling products for children's health

We need an appealing professional web site design and images for a brand new company producing and selling products focused on children’s health. The site will offer information to visitors on the company, the company’s products, and general resources related to children’s health. Additionally the site will offer e-commerce functionality to allow for ordering of the company’s products.
The content and navigation for the site will be generated by programming, such as php or asp, and therefore any images used in the navigation portions of the site should allow for HTML markup to be overlaid rather than having the text built into the image or graphic.
The design must include 2 layouts, one for the landing/home page that includes only top navigation, and an inner page layout that includes both top and left navigation.
The header area of the site should include a place for links to access the visitor’s cart and profile similar to the top sections of quillbarn.com, tervodo.com, and pikmart.com.
The landing page of the site should include some type of “changing” image area where we can include multiple image files for rotation to visitors similar to what is seen at vorlo.com or mallowkite.com. The flash/animation mechanism does not need to be provided (although it would be a plus if it was) but the design must accommodate the space for it.
The company’s colors are Orange (FF9900) and Blue (0066FF) and the logo can be viewed at http://corvanelkids.com/logo.png
All CSS and markup provided must be display consistently in Internet Explorer 7+, FifeFox, Google Chrome, and Safari.
Incorporating social media links (facebook, twitter, etc.) is desirable.
Target Market(s)
Parents who are conscious of health risks associated with children's diets and consumer food products.
Industry/Entity Type
E-Commerce
Look and feel
Each slider illustrates characteristics of the customer's brand and the style your logo design should communicate.

```html
<!DOCTYPE html>
<html lang="en">
<head>
<meta charset="utf-8">
<title>Corvanel Kids — Healthy Children</title>
<link rel="stylesheet" href="https://fonts.googleapis.com/css2?family=Arimo:wght@400;700&family=Playfair+Display:wght@700&display=swap">
<style>
  :root {
    --sky: #86bedd;
    --sky-deep: #6aa9cf;
    --stripe: #3aa7dd;
    --brand-orange: #ff9900;
    --brand-blue: #0066ff;
    --login-green: #1fa85a;
    --login-lime: #b6d836;
    --login-tab: #f6c634;
    --nav-top: #5bbde4;
    --nav-bottom: #2592c7;
    --panel-frame: #e6e6e6;
    --panel-white: #ffffff;
    --tag-grey: #ececec;
    --tag-grey-text: #a9a9a9;
    --chip-orange: #ff8a00;
    --chip-mint: #d6f2ee;
    --chip-pink: #ffb6cf;
    --thumb-green: #8cc63f;
    --thumb-pink: #f6a9c4;
    --thumb-teal: #86d0cf;
    --thumb-orange: #ff8400;
    --story-blue-1: #1f7fc0;
    --story-blue-2: #8cc6e6;
    --story-card: rgba(255,255,255,0.28);
    --headline-red: #d0021b;
    --subhead-blue: #1f5a86;
    --body-green: #203a08;
    --btn-green-1: #9bd33c;
    --btn-green-2: #3f7e0a;
    --card-green-bg: #dbf49a;
    --card-green: #97cd1a;
    --card-green-tab: #4f7d16;
    --card-pink-bg: #ffd2e1;
    --card-pink: #dc9cb4;
    --card-pink-tab: #e4286d;
    --footer: #5790b1;
    --white: #ffffff;
  }
  * { box-sizing: border-box; margin: 0; padding: 0; }
  html, body { width: 1200px; height: 1140px; overflow: hidden; }
  body {
    position: relative;
    font-family: "Arimo", Arial, sans-serif;
    background:
      radial-gradient(ellipse 700px 500px at 200px 120px, rgba(255,255,255,0.35), transparent 70%),
      linear-gradient(180deg, var(--sky-deep) 0%, var(--sky) 40%, var(--sky-deep) 100%);
  }
  .stripe {
    position: absolute; left: 0; width: 1200px; height: 10px;
    background: repeating-linear-gradient(90deg, var(--stripe) 0 10px, #c9ecfb 10px 14px);
  }
  .stripe--top { top: 0; }
  .stripe--bottom { bottom: 0; }
  .abs { position: absolute; }

  /* brand */
  .brand { left: 114px; top: 120px; display: flex; align-items: center; gap: 10px; }
  .brand-dot { width: 34px; height: 34px; border-radius: 50%; background: var(--brand-orange); }
  .brand-name { font-size: 34px; font-weight: 700; color: var(--brand-blue); letter-spacing: -0.5px; }

  /* login */
  .login {
    left: 774px; top: 26px; width: 412px; height: 100px; border-radius: 12px;
    background: linear-gradient(180deg, var(--login-green), var(--login-lime));
    border: 3px solid #f2f6e6; box-shadow: 0 2px 4px rgba(0,0,0,0.2); overflow: hidden;
  }
  .login-tab {
    position: absolute; left: 0; top: 0; width: 72px; height: 100%;
    background: var(--login-tab); clip-path: polygon(0 0, 100% 0, 60% 100%, 0 100%);
  }
  .login-tab-label {
    position: absolute; left: 4px; top: 34px; transform: rotate(-62deg);
    font-weight: 700; font-size: 15px; color: var(--headline-red); letter-spacing: 1px;
  }
  .login-label { position: absolute; font-size: 14px; color: #1d3d1a; }
  .login-input { position: absolute; width: 138px; height: 16px; background: var(--white); border: 1px solid #333; }
  .login-go {
    position: absolute; left: 313px; top: 31px; width: 45px; height: 22px; border-radius: 5px;
    background: linear-gradient(180deg, #ffe89a, #f3b622); color: var(--headline-red);
    font-size: 14px; font-weight: 700; text-align: center; line-height: 22px;
  }
  .login-link { position: absolute; top: 69px; font-size: 14px; font-weight: 700; white-space: nowrap; }

  /* nav */
  .main-nav {
    left: 540px; top: 172px; width: 610px; height: 38px; display: flex;
    background: linear-gradient(180deg, var(--nav-top), var(--nav-bottom));
    border-radius: 5px; box-shadow: 0 2px 3px rgba(0,0,0,0.2);
  }
  .main-nav a {
    color: var(--white); text-decoration: none; font-size: 13px; font-weight: 700;
    display: flex; align-items: center; justify-content: center; height: 100%;
    border-right: 1px solid rgba(255,255,255,0.35); white-space: nowrap;
  }
  .main-nav a:last-child { border-right: 0; }

  /* hero */
  .hero { left: 52px; top: 228px; width: 1106px; height: 540px; background: var(--panel-frame); }
  .hero-inner { position: absolute; left: 8px; top: 8px; width: 1090px; height: 524px; background: var(--panel-white); }
  .hero-tag {
    left: 103px; top: 234px; width: 156px; height: 26px; background: var(--tag-grey);
    color: var(--tag-grey-text); font-size: 13px; font-weight: 700; text-align: center; line-height: 26px;
  }
  .chip { height: 29px; width: 88px; border-radius: 3px; }
  .hero-photo {
    left: 78px; top: 318px; width: 420px; height: 360px;
    background: radial-gradient(ellipse 180px 190px at 55% 50%, #f3cfae, #e7b992 55%, #fbf4ee 80%, #ffffff);
  }
  .thumb { top: 680px; width: 102px; height: 76px; border: 4px solid; border-radius: 5px;
    background: linear-gradient(180deg, #efe3d5, #e2b894); }
  .story {
    left: 568px; top: 242px; width: 573px; height: 509px;
    background: linear-gradient(160deg, var(--story-blue-1), var(--story-blue-2) 70%, #c8e6f6);
  }
  .story-tag {
    left: 608px; top: 282px; width: 110px; height: 22px; border-radius: 4px;
    background: rgba(255,255,255,0.35); color: var(--white); font-size: 15px; line-height: 22px; padding-left: 19px;
  }
  .story-date { left: 616px; top: 311px; color: var(--white); font-size: 13px; }
  .story-card { left: 606px; top: 340px; width: 494px; height: 362px; border-radius: 6px; background: var(--story-card); }
  .story-title {
    left: 624px; top: 362px; font-family: "Playfair Display", Georgia, serif; font-weight: 700;
    font-size: 36px; color: var(--headline-red); letter-spacing: -1.5px; white-space: nowrap;
  }
  .story-sub { left: 640px; top: 432px; width: 400px; font-size: 21px; color: var(--subhead-blue); line-height: 26px; }
  .story-body { left: 635px; top: 516px; width: 440px; font-size: 16px; color: var(--body-green); line-height: 20.5px; }
  .btn-learn {
    left: 638px; top: 646px; width: 122px; height: 27px; border-radius: 6px;
    background: linear-gradient(180deg, var(--btn-green-1), var(--btn-green-2));
    border: 1px solid #d9f2b0; color: var(--white); font-size: 13px; text-align: center; line-height: 25px;
  }

  /* weekly cards */
  .week { top: 791px; width: 544px; height: 191px; border-radius: 6px; }
  .week--green { left: 50px; background: var(--card-green-bg); }
  .week--pink { left: 612px; background: var(--card-pink-bg); }
  .week-tab {
    position: absolute; left: 8px; top: 6px; height: 32px; border-radius: 4px 4px 0 0;
    font-family: "Playfair Display", Georgia, serif; font-weight: 700; font-size: 16px;
    color: var(--white); padding: 0 11px; line-height: 32px; letter-spacing: -0.6px; white-space: nowrap;
  }
  .week-box { position: absolute; left: 8px; top: 37px; width: 526px; height: 146px; border-radius: 0 4px 4px 4px; }
  .week--green .week-tab { background: var(--card-green-tab); }
  .week--green .week-box { background: var(--card-green); }
  .week--pink .week-tab { background: var(--card-pink-tab); }
  .week--pink .week-box { background: var(--card-pink); }
  .week-text { position: absolute; left: 8px; top: 14px; width: 512px; color: var(--white); font-size: 14.5px; line-height: 18px; }
  .btn-read {
    position: absolute; left: 12px; width: 80px; height: 26px; border-radius: 4px;
    color: var(--white); font-size: 11px; text-align: center; line-height: 24px; border: 1px solid #fff;
  }
  .week--green .btn-read { top: 106px; background: linear-gradient(180deg, #b6e05a, #4d7f12); }
  .week--pink .btn-read { top: 104px; background: linear-gradient(180deg, #f79cbc, #e0256a); }

  /* footer */
  .site-footer {
    left: 6px; top: 992px; width: 1183px; height: 129px; border-radius: 4px;
    background: var(--footer); color: var(--white); font-size: 13px; text-align: center;
  }
  .site-footer p { position: absolute; left: 0; width: 100%; white-space: nowrap; }
</style>
</head>
<body>
  <div class="stripe stripe--top"></div>

  <div class="abs brand">
    <span class="brand-dot"></span>
    <span class="brand-name">corvanelkids</span>
  </div>

  <form class="abs login">
    <div class="login-tab"></div>
    <span class="login-tab-label">LOGIN</span>
    <span class="login-label" style="left:84px;top:16px">Username:</span>
    <span class="login-input" style="left:166px;top:16px"></span>
    <span class="login-label" style="left:84px;top:37px">Password:</span>
    <span class="login-input" style="left:166px;top:37px"></span>
    <span class="login-go">Go</span>
    <span class="login-link" style="left:59px;color:var(--headline-red)">Lost Password?</span>
    <span class="login-link" style="left:183px;color:#ffe600;font-size:16px;top:67px">JOIN NOW !</span>
    <span class="login-link" style="left:296px;color:#14380c">Register</span>
  </form>

  <nav class="abs main-nav">
    <a style="width:71px">HOME</a>
    <a style="width:72px">ABOUT</a>
    <a style="width:101px">PRODUCTS</a>
    <a style="width:130px">EXPERT ADVICE</a>
    <a style="width:138px">SPECIAL OFFERS</a>
    <a style="width:98px">CONTACT</a>
  </nav>

  <section class="abs hero">
    <div class="hero-inner"></div>
  </section>
  <div class="abs hero-photo" role="img" aria-label="Photo of a laughing young girl with pigtails resting her face in her hands"></div>
  <div class="abs hero-tag">HEALTHY CHILDREN</div>
  <div class="abs chip" style="left:404px;top:248px;background:var(--chip-orange)"></div>
  <div class="abs chip" style="left:366px;top:282px;background:var(--chip-mint)"></div>
  <div class="abs chip" style="left:458px;top:282px;background:var(--chip-pink)"></div>
  <div class="abs thumb" style="left:70px;border-color:var(--thumb-green)" role="img" aria-label="Thumbnail of the slideshow photo"></div>
  <div class="abs thumb" style="left:194px;border-color:var(--thumb-pink)" role="img" aria-label="Thumbnail of the slideshow photo"></div>
  <div class="abs thumb" style="left:319px;border-color:var(--thumb-teal)" role="img" aria-label="Thumbnail of the slideshow photo"></div>
  <div class="abs thumb" style="left:444px;border-color:var(--thumb-orange)" role="img" aria-label="Thumbnail of the slideshow photo"></div>

  <article>
    <div class="abs story" role="img" aria-label="Blue background with white floral swirl decoration"></div>
    <div class="abs story-tag">ARTICAL</div>
    <div class="abs story-date">September 6</div>
    <div class="abs story-card"></div>
    <h2 class="abs story-title">“Good health”</h2>
    <p class="abs story-sub">Is one of the most important ingredients for a happy and productive life. ...</p>
    <p class="abs story-body">Good health is one of the most important ingredients for a happy and productive life. And yet, many people do not have access to health care and live in conditions that spread disease ....</p>
    <a class="abs btn-learn">Learn More</a>
  </article>

  <section class="abs week week--green">
    <h3 class="week-tab">For your Child this week</h3>
    <div class="week-box">
      <p class="week-text">Mealtime can be a battleground, but with these helpful tips you can teach your child how to be good company.Mealtime can be a battleground, but with these helpful tips you can teach your child how to be good company.</p>
      <a class="btn-read">Read More</a>
    </div>
  </section>

  <section class="abs week week--pink">
    <h3 class="week-tab">For your Child this week</h3>
    <div class="week-box">
      <p class="week-text">Mealtime can be a battleground, but with these helpful tips you can teach your child how to be good company.Mealtime can be a battleground, but with these helpful tips you can teach your child how to be good company.</p>
      <a class="btn-read">Read More</a>
    </div>
  </section>

  <footer class="abs site-footer">
    <p style="top:18px">PRIVACY POLICY | Home | Site Map | Tips &amp; Articles | Expert Advice | Tools &amp; Activities | Products | Special Offers | About Corvanel Kids</p>
    <p style="top:49px">Register | Unsubscribe | Search | Contact Us | Terms &amp; Conditions</p>
    <p style="top:81px">© CORVANEL KIDS All trademarks and other intellectual properties on this site are owned by Corvanel Kids</p>
  </footer>

  <div class="stripe stripe--bottom"></div>
</body>
</html>
```